Lotvantage.com Webpage Design

Design Brief for lotvantage.com (Copy of Brief also in attached Word file)

Name of Website- lotvantage.com (existing logo and look & feel of website to be changed)

Logo - Finalised. The logo files are attached with the brief as “logo.jpeg”. The “Blue- Grey” version of the logo is for use on lighter backgrounds and the “Orange-White” version of the logo is for use on darker backgrounds. (A full Black version of the logo is also attached). Both versions may be used in different parts of the website. All attached files are in .png format.
Status - The website in functional and is undergoing user trials. However, we want to improve the look & feel of the website so at it seems
a. cotemporary,
b. Easy to Navigate
c. professional and
d. Vibrant.

Please visit ‘lotvantage.com’ to check out the website and its functionalities – please use it only as a reference for the features & functions to be provided, however the designer should use a ‘Free Hand’ in designing the composition of various parts of the webpage without getting too influenced by the existing design

Objective of the Website ‘lotvantage.com –
a. It is a portal focussed on listing of ‘Retail’ specific real-estate properties by developers, owners and realty brokers. The properties shall listed under the following four categories-
i. Retail Malls
ii. Shopping Complexes
iii. High-street shops
iv. Retail Warehouses
*refer lotvantage.com for better clarity

b. The abovementioned properties shall be listed either for ‘Sale’ or ‘rent\lease’ or both

c. Users shall visit the site in case they wish to acquire a retail \ shop space either on ‘sale’ or ‘rent’. These Users would be able to specify the ‘Search Criteria’ through the tool-bars provided on the website – the ‘Search Criteria’ shall comprise of ‘Type of space category’, ‘City’, ‘Locality’, transaction type ie ‘Rent \ Sale’ and ‘Area Range’

d. The main revenue model for the website shall be listing fee ( or advertising charges ) payable by those listing their properties on the website.

Three Main Pages of Website (lotvantage.com) that need to be designed -
a. Main Home Page (visit the web link - http://lotvantage.com/ ) - The main home page has the “Search Toolbar” for specifying of Search Criteria by the User. It shall also have the following features & functions-
i. Main Advertising Banner
ii. Featured Projects
iii. New Launches
iv. Toolbar with buttons – ‘Advertise with Us’, ‘Listings Alert’, ‘Lot Mavens’, ‘Advertiser Login’

b. Property Listings Page (visit the web link - http://lotvantage.com/gurgaon-in-india ) - The List of property options that match the Criteria specified by the ‘User’ get displayed on this page.

c. Property Detail Page - When the ‘User’ clicks on the “More….” Button on the ‘Property Listings Page’ (given in point b. above) the web page with the details of the property opens. (For Example – visit the web link - http://lotvantage.com/brevo-Shopping-Complex-brevo-quadrel-gurgaon-636 )

Note:- Please refer to attached ‘Shopping’ related images the designer may use them on the website to provide a look & feel of retail if required – either separately or rotate in a single window

Target Market(s)

Retailers & Investors looking for retail space, Real Estate Brokers, Developers

Industry/Entity Type

Advertising

Number of Pages Required

3 page

Requirements
Must have
• Refer to existing site lotvantage.com -- all the existing functionalities are a must have.
Nice to have
• The Designer may use the retail related images on the website if required for making it more vibrant. Refer attached images Shopping(1-6).jpg

```html
<!DOCTYPE html>
<html lang="en">
<head>
<meta charset="utf-8">
<title>Lotvantage.com – Retail Spaces</title>
<link href="https://fonts.googleapis.com/css2?family=Open+Sans:wght@400;600;700&family=Roboto+Condensed:wght@400;700&display=swap" rel="stylesheet">
<style>
:root{
  --navy:#1d2840;
  --navy-dark:#151d30;
  --orange:#f5921e;
  --blue:#1d8fd8;
  --text:#3b4254;
  --muted:#8a90a0;
  --light:#eef0f3;
  --line:#d9dde4;
  --white:#ffffff;
}
*{box-sizing:border-box;margin:0;padding:0}
html,body{width:1200px;height:2660px;overflow:hidden}
body{font-family:"Open Sans",Arial,sans-serif;color:var(--text);font-size:13px;background:var(--white)}
.wrap{width:1120px;margin:0 auto;position:relative}
h1,h2,h3,h4{font-family:"Roboto Condensed","Arial Narrow",sans-serif}

/* city bar */
.city-bar{height:40px;background:var(--navy);color:#c9cfdb;font-size:12px}
.city-bar .wrap{display:flex;align-items:center;height:40px;gap:10px}
.city-bar span.sep{color:#55607a}

/* header */
.site-header{height:136px;background:var(--white);border-bottom:1px solid var(--line)}
.site-header .wrap{display:flex;align-items:center;height:136px}
.brand{display:flex;align-items:center;gap:12px;font-family:"Open Sans",sans-serif;font-weight:700;font-size:34px;color:var(--navy)}
.brand .dot{width:30px;height:30px;border-radius:50%;background:var(--blue)}
.brand-tag{font-size:10px;color:var(--muted);margin-top:4px;font-weight:400;letter-spacing:.5px}
.main-nav{display:flex;margin-left:auto;gap:0}
.main-nav a{display:block;padding:0 34px;border-left:1px solid var(--line);text-decoration:none;color:var(--navy);font-weight:700;font-size:15px}
.main-nav a small{display:block;font-weight:400;font-size:11px;color:var(--muted);margin-top:3px}
.login-box{margin-left:30px;background:var(--navy);color:#fff;padding:14px 18px;width:200px;text-align:center}
.login-box p{font-size:11px;font-weight:600;margin-bottom:8px}
.login-box .btn-login{display:block;background:var(--orange);font-weight:700;font-size:12px;padding:8px 0;letter-spacing:.5px}
.login-box small{display:block;font-size:10px;color:#aab2c4;margin-top:6px}

/* hero */
.hero{height:424px;position:relative;background:linear-gradient(100deg,#f3efe9 0%,#e9ddcf 38%,#c98d6a 62%,#8e5b45 82%,#5e3d34 100%)}
.hero-copy{position:absolute;left:40px;top:90px;width:400px}
.hero-copy h1{font-size:46px;line-height:1.05;color:var(--navy);font-weight:700;text-transform:uppercase}
.hero-copy p{margin-top:16px;font-size:13px;line-height:1.6;color:#555c6b}
.btn{display:inline-block;text-decoration:none;font-weight:700;font-size:12px;letter-spacing:.5px;color:#fff;text-transform:uppercase}
.btn-blue{background:var(--blue);padding:11px 20px}
.btn-orange{background:var(--orange);padding:11px 22px}
.hero-copy .btn{margin-top:22px}

/* search */
.search-band{height:140px;background:var(--navy);color:#fff}
.search-band .wrap{display:flex;padding-top:22px}
.format{width:300px}
.format h3{font-size:20px;text-transform:uppercase;font-weight:700}
.format ul{list-style:none;display:grid;grid-template-columns:1fr 1fr;gap:8px 14px;margin-top:14px;font-size:12px;color:#cdd3df}
.format li{display:flex;align-items:center;gap:6px}
.format li i{width:12px;height:12px;background:#fff;display:inline-block}
.fields{display:grid;grid-template-columns:260px 260px 140px;gap:8px 16px;margin-left:10px}
.field label{display:block;font-size:11px;color:#cdd3df;margin-bottom:4px}
.field div{height:30px;background:#fff;color:var(--muted);font-size:12px;padding:6px 10px;display:flex;justify-content:space-between}
.search-btn{grid-row:2;grid-column:3;align-self:end;height:30px;background:var(--orange);font-weight:700;font-size:14px;display:flex;align-items:center;justify-content:center}

/* categories */
.categories{height:240px}
.categories .wrap{display:grid;grid-template-columns:repeat(4,1fr);padding-top:36px}
.cat{text-align:center;padding:0 26px;border-right:1px solid var(--line)}
.cat:last-child{border-right:0}
.cat svg{width:48px;height:48px}
.cat h4{color:var(--navy);font-size:17px;text-transform:uppercase;margin:10px 0 8px}
.cat p{font-size:11px;line-height:1.55;color:var(--muted)}
.cat a{display:inline-block;margin-top:10px;font-size:11px;color:var(--blue);font-weight:600;text-decoration:none}

/* featured */
.featured{height:480px;padding-top:40px}
.featured.alt{background:var(--light)}
.section-head{display:flex;align-items:center;gap:14px;border-bottom:2px solid var(--line);padding-bottom:14px}
.section-head h2{font-size:28px;color:var(--navy)}
.section-head span{color:var(--muted);font-size:14px}
.arrows{margin-left:auto;display:flex;gap:6px}
.arrows i{width:24px;height:24px;border-radius:50%;background:#4a5163;display:flex;align-items:center;justify-content:center}
.cards{display:grid;grid-template-columns:repeat(4,1fr);gap:24px;margin-top:28px}
.card{background:#fff;border:1px solid var(--line)}
.card-photo{height:160px;position:relative}
.city-tag{position:absolute;right:0;top:12px;background:var(--orange);color:#fff;font-size:11px;font-weight:700;padding:4px 10px}
.card-body{padding:12px 16px;text-align:center}
.card-body h4{font-size:18px;color:var(--blue)}
.card-body p{font-size:12px;color:var(--muted);margin-top:2px}
.card-body .type{color:var(--navy);font-weight:600;font-size:11px;margin-top:6px}
.card .btn-blue{display:block;text-align:center;padding:10px 0}
.p1{background:linear-gradient(160deg,#c7d8e8,#7d8fa6 55%,#3f4d63)}
.p2{background:linear-gradient(160deg,#cfe0ec,#d9c7a5 55%,#7a6a55)}
.p3{background:linear-gradient(160deg,#d7e3ee,#a7b1ba 50%,#505a66)}
.p4{background:linear-gradient(160deg,#2b3556,#b58a4d 60%,#e6b45c)}

/* widgets */
.widgets{height:420px;background:#fff;border-top:1px solid var(--line)}
.widgets .wrap{display:grid;grid-template-columns:repeat(3,1fr);gap:40px;padding-top:36px}
.widget h3{font-size:26px;color:var(--navy);border-bottom:2px solid var(--line);padding-bottom:10px;margin-bottom:16px}
.widget p{font-size:12px;line-height:1.6;color:var(--muted)}
.alert-intro{display:flex;gap:12px;margin-bottom:14px}
.input{height:30px;border:1px solid var(--line);font-size:12px;color:var(--muted);padding:6px 10px;margin-bottom:9px}
.input.tall{height:56px}
.editor-photo{height:120px;margin-bottom:12px;background:linear-gradient(140deg,#d5c1a8,#9c7e60 60%,#5b4a3c)}
.editor-link{color:var(--blue);font-weight:600}

/* footer */
.site-footer{height:250px;background:var(--navy);color:#c3c9d6}
.site-footer .wrap{display:grid;grid-template-columns:360px 380px 1fr;gap:40px;padding-top:34px}
.site-footer h4{color:#fff;font-size:20px;margin-bottom:14px}
.foot-lists{display:flex;gap:40px}
.foot-lists ul{list-style:none;font-size:12px;line-height:1.9}
.foot-lists li::before{content:"›";color:var(--orange);margin-right:6px}
.site-footer p{font-size:12px;line-height:1.6}
.contact-line{display:flex;gap:10px;font-size:12px;margin-bottom:8px;align-items:flex-start}
.social{display:flex;gap:6px;margin-top:10px}
.social i{width:24px;height:24px;background:#3a4663;display:block}
.footer-brand{position:absolute;right:0;bottom:-30px;display:flex;align-items:center;gap:10px;color:#fff;font-weight:700;font-size:24px}
.footer-brand .dot{width:22px;height:22px;border-radius:50%;background:var(--orange)}
.copyright{height:50px;background:var(--navy-dark);color:#8a93a8;font-size:12px}
.copyright .wrap{line-height:50px}
</style>
</head>
<body>

<div class="city-bar">
  <div class="wrap">
    <span>Bangalore</span><span class="sep">|</span><span>Chennai</span><span class="sep">|</span><span>Greater Noida</span><span class="sep">|</span><span>Gurgaon</span><span class="sep">|</span><span>Hyderabad</span><span class="sep">|</span><span>Jaipur</span><span class="sep">|</span><span>Kolkata</span><span class="sep">|</span><span>Mumbai</span><span class="sep">|</span><span>Noida</span><span class="sep">|</span><span>Pune</span><span class="sep">|</span><span>More</span>
  </div>
</div>

<header class="site-header">
  <div class="wrap">
    <div>
      <div class="brand"><span class="dot"></span>lotvantage</div>
      <div class="brand-tag">RETAIL SPACES FOR RENT, LEASE &amp; SALE</div>
    </div>
    <nav class="main-nav">
      <a href="#">Advertise With Us<small>Standard listing · FREE</small></a>
      <a href="#">Lot Mavens<small>Shop Search Services</small></a>
      <a href="#">Listing Alerts<small>&nbsp;</small></a>
    </nav>
    <div class="login-box">
      <p>Listing Your Property Here</p>
      <span class="btn-login">ADVERTISER LOGIN</span>
      <small>New Advertiser · Register</small>
    </div>
  </div>
</header>

<section class="hero" role="img" aria-label="Photograph of a mother and daughter shopping in a mall, holding shopping bags">
  <div class="hero-copy">
    <h1>Shops at Cox<br>Town Bangalore</h1>
    <p>Lorem Ipsum is simply dummy text of the printing and typesetting industry. Lorem Ipsum has been the industry's standard dummy text ever since the 1500s, when an unknown printer took a galley of type and scrambled.</p>
    <a class="btn btn-blue" href="#">Learn More</a>
  </div>
</section>

<section class="search-band">
  <div class="wrap">
    <div class="format">
      <h3>Select Retail Format</h3>
      <ul>
        <li><i></i>Retail Malls</li><li><i></i>Shopping Complex</li>
        <li><i></i>High Street</li><li><i></i>Retail Warehouse</li>
      </ul>
    </div>
    <div class="fields">
      <div class="field"><label>Sale or Rent Or Both:</label><div>Both<span>▾</span></div></div>
      <div class="field"><label>Select City:</label><div>Select City<span>▾</span></div></div>
      <div></div>
      <div class="field"><label>Select Locality/Micro-Market:</label><div>Select<span>▾</span></div></div>
      <div class="field"><label>Enter Keywords:</label><div>Keyword</div></div>
      <div class="search-btn">SEARCH</div>
    </div>
  </div>
</section>

<section class="categories">
  <div class="wrap">
    <div class="cat">
      <svg viewBox="0 0 48 48"><rect x="6" y="18" width="36" height="24" fill="none" stroke="#1d8fd8" stroke-width="3"/><path d="M4 18 24 6l20 12" fill="none" stroke="#1d8fd8" stroke-width="3"/><rect x="20" y="28" width="8" height="14" fill="#1d8fd8"/></svg>
      <h4>Retail Malls</h4>
      <p>Lorem ipsum dolor sit amet consectetur adipiscing elit, sed eiusmod tempor incididunt et labore magna aliqua.</p>
      <a href="#">Read More...</a>
    </div>
    <div class="cat">
      <svg viewBox="0 0 48 48"><path d="M6 16h36l-4-8H10z" fill="#1d8fd8"/><rect x="8" y="16" width="32" height="26" fill="none" stroke="#1d8fd8" stroke-width="3"/><rect x="14" y="24" width="8" height="18" fill="#1d8fd8"/><rect x="27" y="24" width="8" height="8" fill="#1d8fd8"/></svg>
      <h4>Shopping Complex</h4>
      <p>Lorem ipsum dolor sit amet consectetur adipiscing elit, sed eiusmod tempor incididunt et labore magna aliqua.</p>
      <a href="#">Read More...</a>
    </div>
    <div class="cat">
      <svg viewBox="0 0 48 48"><rect x="6" y="10" width="14" height="32" fill="none" stroke="#1d8fd8" stroke-width="3"/><rect x="24" y="20" width="18" height="22" fill="none" stroke="#1d8fd8" stroke-width="3"/><path d="M4 42h40" stroke="#1d8fd8" stroke-width="3"/></svg>
      <h4>High Street Shops</h4>
      <p>Lorem ipsum dolor sit amet consectetur adipiscing elit, sed eiusmod tempor incididunt et labore magna aliqua.</p>
      <a href="#">Read More...</a>
    </div>
    <div class="cat">
      <svg viewBox="0 0 48 48"><path d="M4 20 24 8l20 12v22H4z" fill="none" stroke="#1d8fd8" stroke-width="3"/><path d="M12 42V26h24v16M12 32h24M12 37h24" fill="none" stroke="#1d8fd8" stroke-width="2.5"/></svg>
      <h4>Retail Warehouses</h4>
      <p>Lorem ipsum dolor sit amet consectetur adipiscing elit, sed eiusmod tempor incididunt et labore magna aliqua.</p>
      <a href="#">Read More...</a>
    </div>
  </div>
</section>

<section class="featured alt">
  <div class="wrap">
    <div class="section-head"><h2>Featured Retail Projects</h2><span>Across India</span>
      <div class="arrows"><i><svg width="10" height="10" viewBox="0 0 10 10"><path d="M7 1 3 5l4 4" stroke="#fff" stroke-width="2" fill="none"/></svg></i><i><svg width="10" height="10" viewBox="0 0 10 10"><path d="M3 1l4 4-4 4" stroke="#fff" stroke-width="2" fill="none"/></svg></i></div>
    </div>
    <div class="cards">
      <div class="card"><div class="card-photo p1" role="img" aria-label="Photograph of a glass-fronted retail building"><span class="city-tag">Surat</span></div><div class="card-body"><h4>Halden</h4><p>Athwa</p><p class="type">SHOPPING COMPLEX</p></div><a class="btn btn-blue" href="#">View The Listing</a></div>
      <div class="card"><div class="card-photo p2" role="img" aria-label="Rendering of a high street shopping block"><span class="city-tag">Faridabad</span></div><div class="card-body"><h4>Verra 81 High Street</h4><p>Sector-81</p><p class="type">SHOPPING COMPLEX</p></div><a class="btn btn-blue" href="#">View The Listing</a></div>
      <div class="card"><div class="card-photo p3" role="img" aria-label="Rendering of a commercial tower with retail podium"><span class="city-tag">Gurgaon</span></div><div class="card-body"><h4>K2K Metropole</h4><p>Sector-65</p><p class="type">SHOPPING COMPLEX</p></div><a class="btn btn-blue" href="#">View The Listing</a></div>
      <div class="card"><div class="card-photo p4" role="img" aria-label="Night view of an illuminated shopping mall"><span class="city-tag">New Delhi</span></div><div class="card-body"><h4>Oriel 24K</h4><p>Sohna Road</p><p class="type">SHOPPING COMPLEX</p></div><a class="btn btn-blue" href="#">View The Listing</a></div>
    </div>
  </div>
</section>

<section class="featured">
  <div class="wrap">
    <div class="section-head"><h2>Featured Retail Projects</h2><span>Across India</span>
      <div class="arrows"><i><svg width="10" height="10" viewBox="0 0 10 10"><path d="M7 1 3 5l4 4" stroke="#fff" stroke-width="2" fill="none"/></svg></i><i><svg width="10" height="10" viewBox="0 0 10 10"><path d="M3 1l4 4-4 4" stroke="#fff" stroke-width="2" fill="none"/></svg></i></div>
    </div>
    <div class="cards">
      <div class="card"><div class="card-photo p1" role="img" aria-label="Photograph of a glass-fronted retail building"><span class="city-tag">Surat</span></div><div class="card-body"><h4>Halden</h4><p>Athwa</p><p class="type">SHOPPING COMPLEX</p></div><a class="btn btn-blue" href="#">View The Listing</a></div>
      <div class="card"><div class="card-photo p2" role="img" aria-label="Rendering of a high street shopping block"><span class="city-tag">Faridabad</span></div><div class="card-body"><h4>Verra 81 High Street</h4><p>Sector-81</p><p class="type">SHOPPING COMPLEX</p></div><a class="btn btn-blue" href="#">View The Listing</a></div>
      <div class="card"><div class="card-photo p3" role="img" aria-label="Rendering of a commercial tower with retail podium"><span class="city-tag">Gurgaon</span></div><div class="card-body"><h4>K2K Metropole</h4><p>Sector-65</p><p class="type">SHOPPING COMPLEX</p></div><a class="btn btn-blue" href="#">View The Listing</a></div>
      <div class="card"><div class="card-photo p4" role="img" aria-label="Night view of an illuminated shopping mall"><span class="city-tag">New Delhi</span></div><div class="card-body"><h4>Oriel 24K</h4><p>Sohna Road</p><p class="type">SHOPPING COMPLEX</p></div><a class="btn btn-blue" href="#">View The Listing</a></div>
    </div>
  </div>
</section>

<section class="widgets">
  <div class="wrap">
    <div class="widget">
      <h3>Listing Alert</h3>
      <div class="alert-intro">
        <svg width="40" height="30" viewBox="0 0 40 30"><rect x="1" y="1" width="38" height="28" fill="none" stroke="#1d8fd8" stroke-width="2"/><path d="M1 1l19 15L39 1" fill="none" stroke="#1d8fd8" stroke-width="2"/></svg>
        <p>Subscribe for fortnightly email updates on new listings &amp; price changes across retail spaces.</p>
      </div>
      <div class="input">Enter your email address</div>
      <div class="input">Select Options ▾</div>
      <div class="input">(select one or more formats)</div>
      <div class="input">Ahmedabad ▾</div>
      <a class="btn btn-orange" href="#">Subscribe</a>
    </div>
    <div class="widget">
      <h3>Editor's Choice</h3>
      <div class="editor-photo" role="img" aria-label="Photograph of a busy shopping arcade interior"></div>
      <p>A "Select" listing of retail properties handpicked by our editors based on their own physical evaluation on parameters &amp; attributes such as location, frontage, footfall, visibility, developer track record and value for money. Read on to check out the current picks for you and your business. <span class="editor-link">Read More...</span></p>
    </div>
    <div class="widget">
      <h3>Lot Mavens</h3>
      <p style="margin-bottom:14px">Post your retail space requirement with us and our experts shall get back with suitable options, guiding you through the whole process. This is a free service.</p>
      <div class="input">Enter your email address</div>
      <div class="input">Mobile</div>
      <div class="input tall">Brief description of requirement</div>
      <a class="btn btn-orange" href="#">Send</a>
    </div>
  </div>
</section>

<footer class="site-footer">
  <div class="wrap">
    <div>
      <h4>About Lotvantage</h4>
      <div class="foot-lists">
        <ul><li>About Us</li><li>Privacy Policy</li><li>Terms of Use</li><li>Contact Us</li><li>Site Map</li></ul>
        <ul><li>Retail Malls</li><li>Shopping Complex</li><li>High Street Shops</li><li>Retail Warehouses</li></ul>
      </div>
    </div>
    <div>
      <h4>Who We Are</h4>
      <p>Lotvantage.com is a specialised web based platform for retail space, featuring properties across India under formats such as Retail Malls, Shopping Complexes, High Street Shops and Retail Warehouses. It is a place that lets retailers, investors and brokers find the right space with ease and confidence in every category. <span style="color:var(--orange)">Read More...</span></p>
    </div>
    <div>
      <h4>Contact Us</h4>
      <div class="contact-line"><svg width="14" height="16" viewBox="0 0 14 16"><path d="M7 15S1 9 1 6a6 6 0 0 1 12 0c0 3-6 9-6 9z" fill="#f5921e"/><circle cx="7" cy="6" r="2" fill="#1d2840"/></svg><span>Unit 512, Meridian Arcade, Sector 44,<br>Gurgaon – 122003</span></div>
      <div class="contact-line"><svg width="14" height="14" viewBox="0 0 14 14"><path d="M3 1l3 3-2 2a8 8 0 0 0 4 4l2-2 3 3-2 2C5 13 1 9 1 3z" fill="#f5921e"/></svg><span>Phone: +91 124 555 0182</span></div>
      <div class="contact-line"><svg width="14" height="12" viewBox="0 0 14 12"><rect x="1" y="1" width="12" height="10" fill="none" stroke="#f5921e" stroke-width="1.5"/><path d="M1 1l6 5 6-5" fill="none" stroke="#f5921e" stroke-width="1.5"/></svg><span>hello@lotvantage.com</span></div>
      <div class="contact-line"><span style="padding-left:24px">Fax: +91 124 555 0183</span></div>
      <div class="social"><i></i><i></i><i></i><i></i></div>
    </div>
    <div class="footer-brand"><span class="dot"></span>lotvantage</div>
  </div>
</footer>
<div class="copyright"><div class="wrap">Copyright © 2015 Lotvantage.com. All rights reserved.</div></div>

</body>
</html>
```